Looking for Landingpage / Website Designer

We are looking for a Web Designer / Developer for our upcoming Start Up Websites. The first project will be a simple responsive business website with a CTA- Button and an optional Newsletter Opt-In. We do aim for a modern online business approach, since we are a young company.

It is necessary to understand, that we need a conversion orientated design, not a wordpress blog with widgets and galleries.

We are currently discussing how it is going to happen and what preferences we need to focus on.

What we know is, that it should be more of a landing page with an option of adding 2 or 3 Navigation points.

We even thought about using services like plumvesta.com or crintofold.com to have an easier approach for future customizations and A/B testing.

We'd love to see how you fit the design/colors to the upcoming logo
(which is not the final version yet )

hope you can do something about that.

For the Structure.

1. Bracket

Slogan plus a preview text of what we are offering. On the right side a video placeholder plus CTA button.

2. Bracket

Illustrating 3 Benefits. On the right side - Opt in for Contact/Newsletter and CTA Button

3. Bracket

Picture with text just like you have it with the testimonial

You can orientate yourself towards to that landing page example as well:

http://cdn2.zorvellink.net/hub/53/file-581676469-png/Blog-Related_Images/plumvesta_landing_page.png?t=1416543075530

If our collaboration is going well, we would like to stay in touch for further projects.
Updates

Reason: There are 3 Design we do really like but, don't fit exactly our needs. 5 Days max.

Reason: For final adjustments.

I just uploaded the final logo :) Thank you for your commitment so far!

Target Market(s)

Our targeted audience could be almost everybody, who looks for an average paid side job (students, unemployed, house wives and whatever you can imagine). Maybe this is enough information for you to get a mere perception of what this is all about.

Industry/Entity Type

Business

Coding

Coded - Design and coding required

Font styles to use
Serif
Sans Serif

Colors
acd037
5c5c5c
33a6d7

Requirements
Must have
• Registration Opt-In
Responsive on any Device
Customizable
A benefits navigation just like in that example I've uploaded.
Nice to have
• As fast as possible ;D

```html
<!DOCTYPE html>
<html lang="en">
<head>
<meta charset="utf-8">
<title>Workvia – Landing Page</title>
<link href="https://fonts.googleapis.com/css2?family=Arvo:wght@400;700&family=Lato:ital,wght@0,400;0,700;1,400&display=swap" rel="stylesheet">
<style>
:root{
  --green:#acd037;
  --gray:#5c5c5c;
  --hero:#6b6b6b;
  --blue:#33a6d7;
  --dark:#474747;
  --text:#4a4a4a;
  --line:#d8d8d8;
  --white:#ffffff;
}
*{margin:0;padding:0;box-sizing:border-box}
html,body{width:870px;height:1200px;overflow:hidden;background:var(--white)}
body{position:relative;font-family:"Lato",Arial,sans-serif;color:var(--text)}

/* header */
.site-header{position:absolute;left:0;top:0;width:870px;height:83px;background:var(--white)}
.brand{position:absolute;left:109px;top:24px;font-family:"Arvo",Georgia,serif;font-weight:400;font-size:28px;color:var(--gray)}
.main-nav a{position:absolute;top:37px;font-size:12.5px;color:#444;text-decoration:none}

/* hero */
.hero{position:absolute;left:0;top:83px;width:870px;height:369px;background:var(--hero)}
.tag{position:absolute;left:106px;height:28px;background:var(--green);color:#3d3d3d;font-family:"Arvo",serif;font-size:20px;line-height:28px;padding-left:13px}
.hero-copy{position:absolute;left:109px;top:133px;width:316px;color:var(--white);font-size:11.4px;line-height:14.5px}
.cta{position:absolute;left:110px;top:207px;width:200px;height:38px;background:var(--blue);color:var(--white);font-size:19px;text-align:center;line-height:38px;border-radius:2px;box-shadow:0 2px 0 #2585b0;text-decoration:none}
.hero-small{position:absolute;color:var(--white);font-size:8px;text-align:center;width:200px;left:107px}
.hero-phone{position:absolute;left:107px;top:296px;width:200px;text-align:center;color:var(--white);font-size:14px}
.video{position:absolute;left:461px;top:98px;width:292px;height:185px;background:#000}
.video-name{position:absolute;left:0;width:100%;top:76px;text-align:center;font-family:"Arvo",serif;font-size:24px;color:#8a8a8a}
.play{position:absolute;left:136px;top:74px}
.controls{position:absolute;left:9px;bottom:5px;width:276px;height:12px}
.arrow{position:absolute;top:179px;width:29px;height:39px;background:#4a4a4a}

/* benefits */
.benefits{position:absolute;left:0;top:452px;width:870px;height:420px;background:var(--green)}
.tab-active{position:absolute;left:72px;top:0;width:231px;height:37px;background:var(--gray);color:var(--white);font-family:"Arvo",serif;font-size:17.5px;text-align:center;line-height:31px;border-radius:0 0 2px 2px}
.tab{position:absolute;left:338px;top:8px;color:var(--white);font-family:"Arvo",serif;font-size:17.5px}
.benefit{position:absolute;width:200px}
.benefit svg{position:absolute;left:0;top:0}
.benefit h3{position:absolute;left:35px;top:-2px;font-family:"Arvo",serif;font-weight:400;font-size:15px;color:var(--white);white-space:nowrap}
.benefit p{position:absolute;left:35px;top:19px;width:155px;font-size:9.6px;line-height:13px;color:var(--white);text-align:justify;hyphens:auto;-webkit-hyphens:auto}

.signup{position:absolute;left:553px;top:68px;width:238px;height:329px;background:var(--white);border-radius:3px;overflow:hidden}
.signup-head{height:40px;background:var(--blue);color:var(--white);font-family:"Arvo",serif;font-size:17.5px;text-align:center;line-height:40px}
.field{position:absolute;left:13px;width:208px;height:34px;border:1px solid #cfcfcf;border-radius:2px;font-family:"Arvo",serif;font-size:9.6px;color:#666;padding:10px 13px}
.submit{position:absolute;left:73px;top:289px;width:101px;height:32px;background:var(--dark);color:var(--green);font-family:"Arvo",serif;font-size:13px;text-align:center;line-height:32px;border-radius:2px}

/* testimonials */
.section-title{position:absolute;left:83px;top:886px;width:279px;height:31px;background:var(--gray);color:var(--white);font-family:"Arvo",serif;font-size:14px;line-height:31px;padding-left:18px}
.review{position:absolute;width:320px;height:110px}
.review .head{position:absolute;left:1px;top:0;display:flex;align-items:baseline;gap:7px;white-space:nowrap}
.review .name{min-width:74px;font-family:"Arvo",serif;font-size:12px;color:var(--blue)}
.review .role{font-size:8.3px;font-style:italic;color:#333}
.review .role b{font-weight:700}
.photo-frame{position:absolute;left:0;top:18px;width:82px;height:82px;border:1px solid var(--line);padding:5px;background:var(--white)}
.photo{width:100%;height:100%;background:linear-gradient(160deg,#b79a80,#5e4a3e)}
.quote{position:absolute;left:96px;top:27px;width:194px;height:56px;border:1px solid var(--line);border-radius:2px;padding:8px 10px;font-size:9.6px;line-height:13px;text-align:justify;color:#555;background:var(--white)}
.quote::before{content:"";position:absolute;left:-6px;top:22px;width:10px;height:10px;background:var(--white);border-left:1px solid var(--line);border-bottom:1px solid var(--line);transform:rotate(45deg)}

.site-footer{position:absolute;left:0;top:1162px;width:870px;height:38px;background:var(--gray);color:var(--white);font-family:Arial,sans-serif;font-size:10px;text-align:center;line-height:38px}
</style>
</head>
<body>

<header class="site-header">
  <div class="brand">Workvia</div>
  <nav class="main-nav">
    <a href="#" style="left:401px">Home</a>
    <a href="#" style="left:459px">About Us</a>
    <a href="#" style="left:534px">Services</a>
    <a href="#" style="left:602px">Testimonials</a>
    <a href="#" style="left:695px">Contact</a>
  </nav>
</header>

<section class="hero">
  <div class="tag" style="top:55px;width:232px">Workvia is the Most</div>
  <div class="tag" style="top:87px;width:312px">Effective Advertising Service</div>
  <p class="hero-copy">Lorem ipsum dolor sit amet, consectetur adipiscing elit, sed do eiusmod tempor incididunt ut labore et dolore magna aliqua. Ut enim ad minim veniam, quis nostrud exercitation ullamco laboris nisi ut aliquip ex ea commodo.</p>
  <a class="cta" href="#">GET STARTED</a>
  <div class="hero-small" style="top:256px">OR</div>
  <div class="hero-small" style="top:279px">SPEAK US TO IN PERSON</div>
  <div class="hero-phone">148 - 260 - 3971</div>

  <div class="video">
    <div class="video-name">Workvia</div>
    <svg class="play" width="22" height="26" viewBox="0 0 22 26"><path d="M3 2 L20 13 L3 24Z" fill="#fff"/></svg>
    <svg class="controls" width="276" height="12" viewBox="0 0 276 12">
      <circle cx="6" cy="6" r="5" fill="none" stroke="#fff" stroke-width="1.3"/>
      <path d="M5 3.5 L8.5 6 L5 8.5Z" fill="#fff"/>
      <path d="M22 4 h2 l3-2.5 v9 l-3-2.5 h-2Z" fill="#fff"/>
      <g fill="#8ac33e"><rect x="32" y="4" width="1.4" height="4"/><rect x="35" y="4" width="1.4" height="4"/><rect x="38" y="4" width="1.4" height="4"/><rect x="41" y="4" width="1.4" height="4"/></g>
      <g fill="#666"><rect x="44" y="4" width="1.4" height="4"/><rect x="47" y="4" width="1.4" height="4"/></g>
      <rect x="74" y="5" width="128" height="2" fill="#555"/>
      <rect x="74" y="5" width="45" height="2" fill="#8ac33e"/>
      <text x="211" y="8.5" font-family="Lato,sans-serif" font-size="6" fill="#fff">01:30 / 04:55</text>
      <rect x="250" y="3" width="8" height="6" fill="none" stroke="#fff" stroke-width="1.2"/>
      <circle cx="269" cy="6" r="3" fill="none" stroke="#fff" stroke-width="2" stroke-dasharray="1.5 1"/>
    </svg>
  </div>

  <div class="arrow" style="left:0"><svg width="29" height="39" viewBox="0 0 29 39"><path d="M19 8 L9 19.5 L19 31" fill="none" stroke="#fff" stroke-width="1.5"/></svg></div>
  <div class="arrow" style="left:841px"><svg width="29" height="39" viewBox="0 0 29 39"><path d="M10 8 L20 19.5 L10 31" fill="none" stroke="#fff" stroke-width="1.5"/></svg></div>
</section>

<section class="benefits">
  <div class="tab-active">Our Benefits</div>
  <div class="tab">Latest News</div>

  <div class="benefit" style="left:86px;top:71px">
    <svg width="26" height="26" viewBox="0 0 26 26" fill="none" stroke="#fff" stroke-width="1.6"><circle cx="13" cy="8" r="6"/><path d="M2 24 c1-7 6-9 11-9 s10 2 11 9Z"/></svg>
    <h3>Lorium Ipsum</h3><p>Duis aute irure dolor in reprehenderit in voluptate velit esse cillum dolore eu fugiat nulla</p>
  </div>
  <div class="benefit" style="left:306px;top:71px">
    <svg width="26" height="26" viewBox="0 0 26 26" fill="none" stroke="#fff" stroke-width="1.6"><circle cx="13" cy="13" r="4"/><circle cx="13" cy="13" r="9" stroke-dasharray="4 2.5"/></svg>
    <h3>Lorium Ipsum</h3><p>Duis aute irure dolor in reprehenderit in voluptate velit esse cillum dolore eu fugiat nulla</p>
  </div>
  <div class="benefit" style="left:86px;top:152px">
    <svg width="26" height="26" viewBox="0 0 26 26" fill="none" stroke="#fff" stroke-width="1.6"><path d="M5 2 h11 l5 5 v17 h-16Z"/><path d="M9 11 h8 M9 15 h8 M9 19 h8"/></svg>
    <h3>Lorium Ipsum</h3><p>Duis aute irure dolor in reprehenderit in voluptate velit esse cillum dolore eu fugiat nulla</p>
  </div>
  <div class="benefit" style="left:306px;top:152px">
    <svg width="26" height="26" viewBox="0 0 26 26" fill="none" stroke="#fff" stroke-width="1.6"><circle cx="13" cy="13" r="10"/><circle cx="13" cy="13" r="5"/><path d="M6 6 l3.5 3.5 M20 6 l-3.5 3.5 M6 20 l3.5-3.5 M20 20 l-3.5-3.5"/></svg>
    <h3>Lorium Ipsum</h3><p>Duis aute irure dolor in reprehenderit in voluptate velit esse cillum dolore eu fugiat nulla</p>
  </div>
  <div class="benefit" style="left:86px;top:233px">
    <svg width="26" height="26" viewBox="0 0 26 26" fill="none" stroke="#fff" stroke-width="1.6"><rect x="2" y="6" width="22" height="15"/><path d="M2 6 l11 9 l11-9 M2 21 l8-7 M24 21 l-8-7"/></svg>
    <h3>Lorium Ipsum</h3><p>Duis aute irure dolor in reprehenderit in voluptate velit esse cillum dolore eu fugiat nulla</p>
  </div>
  <div class="benefit" style="left:306px;top:233px">
    <svg width="26" height="26" viewBox="0 0 26 26" fill="none" stroke="#fff" stroke-width="1.6"><path d="M13 2 a7.5 7.5 0 0 1 4 14 v4 h-8 v-4 a7.5 7.5 0 0 1 4-14Z"/><path d="M10 23 h6"/></svg>
    <h3>Lorium Ipsum</h3><p>Duis aute irure dolor in reprehenderit in voluptate velit esse cillum dolore eu fugiat nulla</p>
  </div>
  <div class="benefit" style="left:86px;top:321px">
    <svg width="26" height="26" viewBox="0 0 26 26" fill="none" stroke="#fff" stroke-width="1.6"><circle cx="13" cy="13" r="11"/><path d="M7.5 13 l4 4 l7-8"/></svg>
    <h3>Lorium Ipsum</h3><p>Duis aute irure dolor in reprehenderit in voluptate velit esse cillum dolore eu fugiat nulla</p>
  </div>
  <div class="benefit" style="left:306px;top:321px">
    <svg width="26" height="26" viewBox="0 0 26 26" fill="none" stroke="#fff" stroke-width="1.6"><rect x="2" y="2" width="22" height="22"/><circle cx="8.5" cy="8.5" r="2.5"/><path d="M2 20 l7-7 l5 5 l4-4 l6 6"/></svg>
    <h3>Lorium Ipsum</h3><p>Duis aute irure dolor in reprehenderit in voluptate velit esse cillum dolore eu fugiat nulla</p>
  </div>

  <form class="signup">
    <div class="signup-head">Contact / News Letter</div>
    <div class="field" style="top:50px">Name</div>
    <div class="field" style="top:94px">Email</div>
    <div class="field" style="top:138px">Phone</div>
    <div class="field" style="top:182px">Zip code</div>
    <div class="field" style="top:226px;height:56px">Message</div>
    <div class="submit">Submit</div>
  </form>
</section>

<div class="section-title">Whats Our Customers have to say</div>

<article class="review" style="left:100px;top:934px">
  <div class="head"><span class="name">Milo Brandt</span><span class="role">Director of E- Commerce - <b>Brightcrumb</b></span></div>
  <div class="photo-frame"><div class="photo" role="img" aria-label="Portrait photo of Milo Brandt"></div></div>
  <div class="quote">Duis aute irure dolor in reprehenderit in voluptate velit esse cillum dolore eu fugiat nulla</div>
</article>
<article class="review" style="left:478px;top:934px">
  <div class="head"><span class="name">Carla Nuvens</span><span class="role">Director of E- Commerce - <b>Brightcrumb</b></span></div>
  <div class="photo-frame"><div class="photo" role="img" aria-label="Portrait photo of Carla Nuvens" style="background:linear-gradient(160deg,#a07a64,#2e2622)"></div></div>
  <div class="quote">Duis aute irure dolor in reprehenderit in voluptate velit esse cillum dolore eu fugiat nulla</div>
</article>
<article class="review" style="left:100px;top:1051px">
  <div class="head"><span class="name">Tessa</span><span class="role">Director of E- Commerce - <b>Brightcrumb</b></span></div>
  <div class="photo-frame"><div class="photo" role="img" aria-label="Portrait photo of Tessa" style="background:linear-gradient(160deg,#d8c19a,#6fa3a8)"></div></div>
  <div class="quote">Duis aute irure dolor in reprehenderit in voluptate velit esse cillum dolore eu fugiat nulla</div>
</article>
<article class="review" style="left:478px;top:1051px">
  <div class="head"><span class="name">Henrik Vale</span><span class="role">Director of E- Commerce - <b>Brightcrumb</b></span></div>
  <div class="photo-frame"><div class="photo" role="img" aria-label="Portrait photo of Henrik Vale" style="background:linear-gradient(160deg,#9b8f86,#2d2f36)"></div></div>
  <div class="quote">Duis aute irure dolor in reprehenderit in voluptate velit esse cillum dolore eu fugiat nulla</div>
</article>

<footer class="site-footer">© 2014 Compnay Name,All Rights Reserved</footer>

</body>
</html>
```